Warm Hands Close Deals.

Sub: how friendliness wins every bargain.

The book talks about what you need to do to achieves a better atmosphere and what you need to do warm your customer. It provides techniques on how to talk, move and about how to create rapport using content, hobbies, common interests and so on. All to increase success in selling something, convincing somebody and being liked much more. It extends to the claim that convincing your spouse to chose your favorite movie rather than hers or to pick that vacation sport over the other one would also a sale, not a commercial sale but an important one too. And that you can achieve these kind of success too using the information from the book. However this is NOT a self help book but a business book!

Business

```html
<!DOCTYPE html>
<html lang="en">
<head>
<meta charset="utf-8">
<title>Warm Hands Close Deals. — Book Cover</title>
<link rel="stylesheet" href="https://fonts.googleapis.com/css2?family=Bebas+Neue&display=swap">
<style>
  :root {
    --teal: #1ec3b3;
    --teal-deep: #16b3a4;
    --teal-glow: #a9f0e6;
    --white: #ffffff;
    --ink: #0b0b0b;
    --suit-light: #a7a9aa;
    --suit-dark: #5f6263;
  }
  html, body {
    margin: 0;
    padding: 0;
    overflow: hidden;
    background: var(--teal);
  }
  .cover {
    position: relative;
    width: 802px;
    height: 1200px;
    overflow: hidden;
    background:
      radial-gradient(ellipse 420px 360px at 50% 560px, var(--teal-glow) 0%, rgba(169,240,230,0) 100%),
      linear-gradient(180deg, var(--teal) 0%, var(--teal-deep) 100%);
    font-family: "Bebas Neue", "Oswald", sans-serif;
  }
  .cover__title {
    position: absolute;
    top: 6px;
    left: 0;
    width: 100%;
    margin: 0;
    text-align: center;
    color: var(--white);
    font-weight: 400;
    font-size: 138px;
    line-height: 124px;
    letter-spacing: 1px;
  }
  .cover__title-accent { color: var(--ink); }
  .cover__band {
    position: absolute;
    top: 360px;
    left: 0;
    width: 100%;
    height: 84px;
    background: var(--white);
    display: flex;
    align-items: center;
    justify-content: center;
  }
  .cover__subtitle {
    margin: 0;
    color: var(--teal);
    font-size: 52px;
    letter-spacing: 1px;
    font-weight: 400;
    padding-top: 6px;
  }
  .cover__figure {
    position: absolute;
    left: 140px;
    top: 515px;
    width: 620px;
    height: 600px;
    border-radius: 240px 240px 20px 20px;
    background: linear-gradient(180deg, var(--suit-light) 0%, var(--suit-dark) 100%);
  }
  .cover__author {
    position: absolute;
    bottom: 14px;
    left: 0;
    width: 100%;
    margin: 0;
    text-align: center;
    color: var(--white);
    font-size: 70px;
    letter-spacing: 1px;
    font-weight: 400;
  }
</style>
</head>
<body>
  <main class="cover">
    <h1 class="cover__title">WARM <span class="cover__title-accent">HANDS</span><br>CLOSE DEALS.</h1>
    <div class="cover__band">
      <p class="cover__subtitle">HOW FRIENDLINESS WINS EVERY BARGAIN.</p>
    </div>
    <div class="cover__figure" role="img" aria-label="Photo of a businessman in a grey suit and striped tie holding a white card with a smiley drawn on it in front of his face"></div>
    <p class="cover__author">MARTIN HOLLOWAY</p>
  </main>
</body>
</html>
```